Bref créative
Halden Byte Solutions - Stationery
Business Cards, Letter Head & Envelopes
Professional
Gordon Pelley
President
379 Cobble Lane Suite 4150
Sudbury, MA 01776
gpelley@halden-byte.com
www.halden-byte.com

```html
<!DOCTYPE html>
<html lang="en">
<head>
<meta charset="utf-8">
<title>Halden Byte Solutions – Stationery</title>
<link rel="stylesheet" href="https://fonts.googleapis.com/css2?family=Arimo:wght@400;700&display=swap">
<style>
  :root {
    --backdrop: #a7a8aa;
    --backdrop-edge: #c4c5c7;
    --paper: #ffffff;
    --brand-red: #9b2320;
    --accent-red: #b52a25;
    --ink: #4a4a4a;
    --ink-soft: #8a8a8a;
    --faint-mark: #f3e3e1;
    --fold-line: #c9c9c9;
  }
  * { margin: 0; padding: 0; box-sizing: border-box; }
  html, body { width: 1200px; height: 626px; overflow: hidden; }
  body {
    background: var(--backdrop);
    font-family: "Arimo", Arial, sans-serif;
    color: var(--ink);
    position: relative;
  }
  .canvas-frame {
    position: absolute; inset: 6px;
    border: 2px solid var(--backdrop-edge);
  }
  .sheet {
    position: absolute;
    background: var(--paper);
    box-shadow: 1px 2px 4px rgba(0,0,0,.25);
    overflow: hidden;
  }
  .brand { position: absolute; display: flex; align-items: center; gap: 5px; }
  .brand-square { background: var(--brand-red); flex: none; }
  .brand-name { color: var(--brand-red); font-weight: 400; white-space: nowrap; }
  .brand-tagline { position: absolute; color: var(--ink-soft); white-space: nowrap; }
  .accent-bar { position: absolute; left: 0; width: 6px; background: var(--accent-red); }
  .contact { position: absolute; color: var(--ink); line-height: 1.45; white-space: nowrap; }
  .web { position: absolute; color: var(--ink); white-space: nowrap; }
  .faint-mark { position: absolute; background: var(--faint-mark); opacity: .7; }

  /* Business card */
  .business-card { left: 34px; top: 305px; width: 158px; height: 79px; }
  .business-card .brand { left: 9px; top: 11px; }
  .business-card .brand-square { width: 11px; height: 11px; }
  .business-card .brand-name { font-size: 9px; }
  .business-card .brand-tagline { left: 25px; top: 25px; font-size: 4px; }
  .business-card .accent-bar { top: 44px; height: 18px; width: 4px; }
  .business-card .contact { left: 9px; top: 44px; font-size: 4px; }
  .business-card .holder { position: absolute; right: 10px; top: 51px; text-align: right; font-size: 4.5px; line-height: 1.4; }
  .business-card .holder strong { display: block; font-weight: 700; }

  /* Letterhead */
  .letterhead { left: 233px; top: 29px; width: 396px; height: 564px; }
  .letterhead .brand { left: 24px; top: 36px; }
  .letterhead .brand-square { width: 20px; height: 20px; }
  .letterhead .brand-name { font-size: 15px; }
  .letterhead .brand-tagline { left: 49px; top: 59px; font-size: 6px; }
  .letterhead .faint-mark { left: 118px; top: 270px; width: 130px; height: 120px; }
  .letterhead .accent-bar { top: 439px; height: 48px; }
  .letterhead .contact { left: 22px; top: 440px; font-size: 5.5px; }
  .letterhead .web { right: 20px; bottom: 56px; font-size: 5.5px; }

  /* Envelope back */
  .envelope-back { left: 679px; top: 240px; width: 487px; height: 144px; }
  .envelope-back svg { position: absolute; inset: 0; }

  /* Envelope front */
  .envelope-front { left: 679px; top: 401px; width: 487px; height: 187px; }
  .envelope-front .brand { left: 20px; top: 35px; }
  .envelope-front .brand-square { width: 17px; height: 17px; }
  .envelope-front .brand-name { font-size: 12px; }
  .envelope-front .brand-tagline { left: 42px; top: 54px; font-size: 5px; }
  .envelope-front .faint-mark { left: 232px; top: 62px; width: 96px; height: 90px; }
  .envelope-front .accent-bar { top: 102px; height: 44px; }
  .envelope-front .contact { left: 19px; top: 103px; font-size: 5.5px; }
  .envelope-front .web { right: 18px; bottom: 28px; font-size: 5.5px; }
</style>
</head>
<body>
  <div class="canvas-frame"></div>

  <section class="sheet business-card" aria-label="Business card">
    <div class="brand"><span class="brand-square"></span><span class="brand-name">Halden Byte Solutions</span></div>
    <div class="brand-tagline">Smart data, solid service</div>
    <div class="accent-bar"></div>
    <div class="contact">
      379 Cobble Lane Suite 4150<br>
      Sudbury, MA 01776<br>
      T 978 555 0142<br>
      gpelley@halden-byte.com
    </div>
    <div class="holder"><strong>Gordon Pelley</strong>President<br>www.halden-byte.com</div>
  </section>

  <section class="sheet letterhead" aria-label="Letterhead">
    <div class="brand"><span class="brand-square"></span><span class="brand-name">Halden Byte Solutions</span></div>
    <div class="brand-tagline">Smart data, solid service</div>
    <div class="faint-mark"></div>
    <div class="accent-bar"></div>
    <div class="contact">
      379 Cobble Lane Suite 4150<br>
      Sudbury, MA 01776<br>
      T 978 555 0142<br>
      gpelley@halden-byte.com
    </div>
    <div class="web">www.halden-byte.com</div>
  </section>

  <section class="sheet envelope-back" aria-label="Envelope back">
    <svg width="487" height="144" viewBox="0 0 487 144">
      <polyline points="0,12 243,62 487,12" fill="none" stroke="var(--fold-line)" stroke-width="1"/>
      <line x1="0" y1="12" x2="487" y2="12" stroke="var(--fold-line)" stroke-width="0.6"/>
    </svg>
  </section>

  <section class="sheet envelope-front" aria-label="Envelope front">
    <div class="brand"><span class="brand-square"></span><span class="brand-name">Halden Byte Solutions</span></div>
    <div class="brand-tagline">Smart data, solid service</div>
    <div class="faint-mark"></div>
    <div class="accent-bar"></div>
    <div class="contact">
      379 Cobble Lane Suite 4150<br>
      Sudbury, MA 01776<br>
      T 978 555 0142<br>
      gpelley@halden-byte.com
    </div>
    <div class="web">www.halden-byte.com</div>
  </section>
</body>
</html>
```